Web Dashboard for manufacturing data

We need a dashboard for website to show statistical information on buttons/cards/tiles. There will be 12 buttons on the screen (laptop, tablet) On these buttons there are several key pieces of information on each button. 1) Largest info is % 0-100%. 2) 4 status colours neutral, green, yellow, red. 3) Title- up to 20 characters 4) target here is an example... target=above 90%.- When these buttons are tapped, they take user to more info for that specific data.
1 page

```html
<!DOCTYPE html>
<html lang="en">
<head>
<meta charset="utf-8">
<title>Manufacturing Dashboard</title>
<link href="https://fonts.googleapis.com/css2?family=Poppins:wght@400;600;700&display=swap" rel="stylesheet">
<style>
:root{
  --bg-dark:#2a1206;
  --bg-mid:#7a3a0e;
  --bg-light:#a65a1c;
  --card:#ffffff;
  --title:#3a3330;
  --track:#dedede;
  --bar:#555555;
  --green:#23835a;
  --red:#fb4b4b;
  --yellow:#fdcb3c;
  --neutral:#453a37;
}
*{margin:0;padding:0;box-sizing:border-box}
html,body{width:1200px;height:883px;overflow:hidden}
body{
  font-family:'Poppins',sans-serif;
  background:radial-gradient(ellipse at 50% 50%,var(--bg-light) 0%,var(--bg-mid) 45%,var(--bg-dark) 100%);
  position:relative;
}
.dashboard{position:absolute;left:0;top:0;width:1200px;height:883px}
.tile{
  position:absolute;width:242px;height:232px;
  background:var(--card);border-radius:8px;
  text-decoration:none;color:inherit;display:block;
}
.tile-title{
  position:absolute;left:0;right:0;top:15px;
  text-align:center;font-weight:600;font-size:20px;line-height:22px;
  letter-spacing:.4px;color:var(--title);
}
.gauge{position:absolute;left:51px;top:64px;width:140px;height:110px;overflow:visible}
.gauge-track{fill:none;stroke:var(--track);stroke-width:6.5}
.gauge-value{fill:none;stroke-width:6.5}
.gauge-text{position:absolute;left:0;right:0;top:103px;text-align:center;font-size:37px;line-height:44px;font-weight:400;letter-spacing:.5px}
.scale-min,.scale-max{position:absolute;top:143px;font-size:16px;color:var(--title)}
.scale-min{left:50px}
.scale-max{left:182px}
.target{position:absolute;left:21px;top:202px;width:158px;height:6px;border-radius:3px;background:var(--track);overflow:hidden}
.target-fill{height:100%;background:var(--bar);border-radius:3px}
.target-label{position:absolute;left:186px;top:195px;font-size:14px;font-weight:700}
.green{color:var(--green)} .green .gauge-value{stroke:var(--green)}
.red{color:var(--red)} .red .gauge-value{stroke:var(--red)}
.yellow{color:var(--yellow)} .yellow .gauge-value{stroke:var(--yellow)}
.neutral{color:var(--neutral)} .neutral .gauge-value{stroke:var(--neutral)}
.lbl-green{color:var(--green)} .lbl-red{color:var(--red)} .lbl-yellow{color:var(--yellow)} .lbl-neutral{color:var(--neutral)}
</style>
</head>
<body>
<main class="dashboard">

<!-- Row 1 -->
<a class="tile green" href="#" style="left:74px;top:64px">
  <div class="tile-title">Excepteur Sint<br>Occaecat</div>
  <svg class="gauge" viewBox="0 0 140 110"><path class="gauge-track" d="M24.9 100.5 A58 58 0 1 1 115.1 100.5" pathLength="100"/><path class="gauge-value" d="M24.9 100.5 A58 58 0 1 1 115.1 100.5" pathLength="100" stroke-dasharray="90 100"/></svg>
  <div class="gauge-text">90%</div><span class="scale-min">0</span><span class="scale-max">100</span>
  <div class="target"><div class="target-fill" style="width:80%"></div></div><span class="target-label lbl-green">80%</span>
</a>

<a class="tile red" href="#" style="left:344px;top:64px">
  <div class="tile-title">Excepteur Sint<br>Occaecat</div>
  <svg class="gauge" viewBox="0 0 140 110"><path class="gauge-track" d="M24.9 100.5 A58 58 0 1 1 115.1 100.5" pathLength="100"/><path class="gauge-value" d="M24.9 100.5 A58 58 0 1 1 115.1 100.5" pathLength="100" stroke-dasharray="79 100"/></svg>
  <div class="gauge-text">79%</div><span class="scale-min">0</span><span class="scale-max">100</span>
  <div class="target"><div class="target-fill" style="width:80%"></div></div><span class="target-label lbl-red">90%</span>
</a>

<a class="tile yellow" href="#" style="left:616px;top:64px">
  <div class="tile-title">Excepteur Sint<br>Occaecat</div>
  <svg class="gauge" viewBox="0 0 140 110"><path class="gauge-track" d="M24.9 100.5 A58 58 0 1 1 115.1 100.5" pathLength="100"/><path class="gauge-value" d="M24.9 100.5 A58 58 0 1 1 115.1 100.5" pathLength="100" stroke-dasharray="75 100"/></svg>
  <div class="gauge-text">75%</div><span class="scale-min">0</span><span class="scale-max">100</span>
  <div class="target"><div class="target-fill" style="width:80%"></div></div><span class="target-label lbl-yellow">80%</span>
</a>

<a class="tile neutral" href="#" style="left:886px;top:64px">
  <div class="tile-title">Excepteur Sint<br>Occaecat</div>
  <svg class="gauge" viewBox="0 0 140 110"><path class="gauge-track" d="M24.9 100.5 A58 58 0 1 1 115.1 100.5" pathLength="100"/><path class="gauge-value" d="M24.9 100.5 A58 58 0 1 1 115.1 100.5" pathLength="100" stroke-dasharray="80 100"/></svg>
  <div class="gauge-text">80%</div><span class="scale-min">0</span><span class="scale-max">100</span>
  <div class="target"><div class="target-fill" style="width:80%"></div></div><span class="target-label lbl-neutral">80%</span>
</a>

<!-- Row 2 -->
<a class="tile yellow" href="#" style="left:74px;top:326px">
  <div class="tile-title">Excepteur Sint<br>Occaecat</div>
  <svg class="gauge" viewBox="0 0 140 110"><path class="gauge-track" d="M24.9 100.5 A58 58 0 1 1 115.1 100.5" pathLength="100"/><path class="gauge-value" d="M24.9 100.5 A58 58 0 1 1 115.1 100.5" pathLength="100" stroke-dasharray="100 100"/></svg>
  <div class="gauge-text">100%</div><span class="scale-min">0</span><span class="scale-max">100</span>
  <div class="target"><div class="target-fill" style="width:80%"></div></div><span class="target-label lbl-yellow">80%</span>
</a>

<a class="tile neutral" href="#" style="left:344px;top:326px">
  <div class="tile-title">Excepteur Sint<br>Occaecat</div>
  <svg class="gauge" viewBox="0 0 140 110"><path class="gauge-track" d="M24.9 100.5 A58 58 0 1 1 115.1 100.5" pathLength="100"/><path class="gauge-value" d="M24.9 100.5 A58 58 0 1 1 115.1 100.5" pathLength="100" stroke-dasharray="96 100"/></svg>
  <div class="gauge-text">96%</div><span class="scale-min">0</span><span class="scale-max">100</span>
  <div class="target"><div class="target-fill" style="width:80%"></div></div><span class="target-label lbl-neutral">80%</span>
</a>

<a class="tile green" href="#" style="left:616px;top:326px">
  <div class="tile-title">Excepteur Sint<br>Occaecat</div>
  <svg class="gauge" viewBox="0 0 140 110"><path class="gauge-track" d="M24.9 100.5 A58 58 0 1 1 115.1 100.5" pathLength="100"/><path class="gauge-value" d="M24.9 100.5 A58 58 0 1 1 115.1 100.5" pathLength="100" stroke-dasharray="78 100"/></svg>
  <div class="gauge-text">78%</div><span class="scale-min">0</span><span class="scale-max">100</span>
  <div class="target"><div class="target-fill" style="width:80%"></div></div><span class="target-label lbl-green">80%</span>
</a>

<a class="tile red" href="#" style="left:886px;top:326px">
  <div class="tile-title">Excepteur Sint<br>Occaecat</div>
  <svg class="gauge" viewBox="0 0 140 110"><path class="gauge-track" d="M24.9 100.5 A58 58 0 1 1 115.1 100.5" pathLength="100"/><path class="gauge-value" d="M24.9 100.5 A58 58 0 1 1 115.1 100.5" pathLength="100" stroke-dasharray="78 100"/></svg>
  <div class="gauge-text">78%</div><span class="scale-min">0</span><span class="scale-max">100</span>
  <div class="target"><div class="target-fill" style="width:80%"></div></div><span class="target-label lbl-neutral">80%</span>
</a>

<!-- Row 3 -->
<a class="tile green" href="#" style="left:74px;top:590px">
  <div class="tile-title">Excepteur Sint<br>Occaecat</div>
  <svg class="gauge" viewBox="0 0 140 110"><path class="gauge-track" d="M24.9 100.5 A58 58 0 1 1 115.1 100.5" pathLength="100"/><path class="gauge-value" d="M24.9 100.5 A58 58 0 1 1 115.1 100.5" pathLength="100" stroke-dasharray="70 100"/></svg>
  <div class="gauge-text">70%</div><span class="scale-min">0</span><span class="scale-max">100</span>
  <div class="target"><div class="target-fill" style="width:80%"></div></div><span class="target-label lbl-green">80%</span>
</a>

<a class="tile red" href="#" style="left:344px;top:590px">
  <div class="tile-title">Excepteur Sint<br>Occaecat</div>
  <svg class="gauge" viewBox="0 0 140 110"><path class="gauge-track" d="M24.9 100.5 A58 58 0 1 1 115.1 100.5" pathLength="100"/><path class="gauge-value" d="M24.9 100.5 A58 58 0 1 1 115.1 100.5" pathLength="100" stroke-dasharray="100 100"/></svg>
  <div class="gauge-text">100%</div><span class="scale-min">0</span><span class="scale-max">100</span>
  <div class="target"><div class="target-fill" style="width:80%"></div></div><span class="target-label lbl-red">80%</span>
</a>

<a class="tile yellow" href="#" style="left:616px;top:590px">
  <div class="tile-title">Excepteur Sint<br>Occaecat</div>
  <svg class="gauge" viewBox="0 0 140 110"><path class="gauge-track" d="M24.9 100.5 A58 58 0 1 1 115.1 100.5" pathLength="100"/><path class="gauge-value" d="M24.9 100.5 A58 58 0 1 1 115.1 100.5" pathLength="100" stroke-dasharray="90 100"/></svg>
  <div class="gauge-text">90%</div><span class="scale-min">0</span><span class="scale-max">100</span>
  <div class="target"><div class="target-fill" style="width:80%"></div></div><span class="target-label lbl-yellow">80%</span>
</a>

<a class="tile neutral" href="#" style="left:886px;top:590px">
  <div class="tile-title">Excepteur Sint<br>Occaecat</div>
  <svg class="gauge" viewBox="0 0 140 110"><path class="gauge-track" d="M24.9 100.5 A58 58 0 1 1 115.1 100.5" pathLength="100"/><path class="gauge-value" d="M24.9 100.5 A58 58 0 1 1 115.1 100.5" pathLength="100" stroke-dasharray="78 100"/></svg>
  <div class="gauge-text">78%</div><span class="scale-min">0</span><span class="scale-max">100</span>
  <div class="target"><div class="target-fill" style="width:80%"></div></div><span class="target-label lbl-neutral">80%</span>
</a>

</main>
</body>
</html>
```